Grey orchard secret

UPDATED BRIEF:
I'm just updating the brief to enable any new submissions to come up with their own ideas. I have tried to offer my ideas below, but I am too close to the project therefor any new submissions are probably best using your talent. The main thing is it stands out and someone would want to buy it against the competition. All submissions have been excellent, so to be fair I will put the winning vote to family and friends. I am too close and biased to make the final choice.
This book is part memoire/ part biography/ part diary/ part self help.
My world is falling apart. I use the analogy of being lost at see. This book is my ships log. It could be a torn out PAGE of the log, a POSTER, or A MESSAGE a bottle.
It needs to be clear in the title, so GREY ORCHARD SECRET needs to stand out. BOO could be a wax seal, like a stamp. 'You've found the' and 'We're dancing at dusk' are less important. The title is: BOO You've found the GREY ORCHARD SECRET We're dancing at dusk.
Other subliminal random words are: family, paranoia, sex addiction, depression, marriage, divorce.
The other idea is flame red. Needs to be subtle to show my life is going up in flames. The diary page/poster/note should be singed or worn.
Ideally text font should be bespoke. Whether some or all are slightly wonky to show that my life is falling apart.
Octopus bottom left with tentacles spread over spine is a firm favourite
Text on spine needs to be large to stand out. Open to suggestions but nothing over simple.Good luck

Target Market(s)

30-60 years

Colors

Requirements
Must have
• Book size. I'm assuming: 21.5cm x 13.5cm x 2.5cm. I will need ebook version and paperback version. ISBN details will follow later

```html
<!DOCTYPE html>
<html lang="en">
<head>
<meta charset="utf-8">
<title>Grey Orchard Secret – Book Cover</title>
<link rel="stylesheet" href="https://fonts.googleapis.com/css2?family=Questrial&display=swap">
<style>
  :root {
    --backdrop: #cfdff1;
    --sky-light: #9fd0ee;
    --sky-mid: #4f9fd6;
    --sea-surface: #2f6fc0;
    --sea-deep: #0f3a92;
    --sea-abyss: #0a2a78;
    --parchment-light: #efe3c2;
    --parchment-dark: #c9ad78;
    --title-white: #ffffff;
    --title-shadow: rgba(10, 30, 70, 0.55);
  }
  * { margin: 0; padding: 0; box-sizing: border-box; }
  html, body {
    width: 1200px;
    height: 983px;
    overflow: hidden;
    background: var(--backdrop);
  }
  .canvas {
    position: relative;
    width: 1200px;
    height: 983px;
  }
  .book-cover {
    position: absolute;
    left: 317px;
    top: 52px;
    width: 566px;
    height: 880px;
    overflow: hidden;
    box-shadow: 0 12px 30px rgba(20, 50, 100, 0.18);
  }
  .cover-artwork {
    position: absolute;
    inset: 0;
    background:
      linear-gradient(180deg,
        var(--sky-mid) 0%,
        var(--sky-light) 28%,
        #bfe0f3 40%,
        var(--sky-mid) 48%,
        var(--sea-surface) 51%,
        var(--sea-deep) 68%,
        var(--sea-abyss) 100%);
  }
  .parchment-edge {
    position: absolute;
    left: 0;
    width: 100%;
    background: linear-gradient(180deg, var(--parchment-light), var(--parchment-dark));
  }
  .parchment-edge--top { top: 0; height: 52px; }
  .parchment-edge--bottom {
    bottom: 0; height: 43px;
    background: linear-gradient(0deg, var(--parchment-light), var(--parchment-dark));
  }
  .cover-title { font-weight: 400; }
  .title-line {
    position: absolute;
    left: 0;
    width: 100%;
    text-align: center;
    font-family: "Questrial", "Century Gothic", sans-serif;
    color: var(--title-white);
    text-transform: uppercase;
    line-height: 1;
    letter-spacing: 0.01em;
    text-shadow: 2px 3px 4px var(--title-shadow);
    transform: translateY(-50%);
    white-space: nowrap;
  }
  .title-line--seal { top: 140px; font-size: 100px; }
  .title-line--lead { font-size: 52px; }
  .title-line--lead-1 { top: 230px; }
  .title-line--lead-2 { top: 308px; }
  .title-line--lead-3 { top: 386px; }
  .title-line--main { font-size: 62px; letter-spacing: -0.01em; }
  .title-line--main-1 { top: 476px; }
  .title-line--main-2 { top: 546px; }
  .title-line--tail { font-size: 52px; }
  .title-line--tail-1 { top: 636px; }
  .title-line--tail-2 { top: 712px; }
</style>
</head>
<body>
  <main class="canvas">
    <section class="book-cover" aria-label="Book cover: Grey Orchard Secret">
      <div class="cover-artwork" role="img" aria-label="Photograph of a corked glass bottle floating at the sea surface, sky above and deep blue water with bubbles below"></div>
      <div class="parchment-edge parchment-edge--top" role="img" aria-label="Torn aged parchment edge"></div>
      <div class="parchment-edge parchment-edge--bottom" role="img" aria-label="Torn aged parchment edge"></div>

      <h1 class="cover-title">
        <span class="title-line title-line--seal">Boo</span>
        <span class="title-line title-line--lead title-line--lead-1">You've</span>
        <span class="title-line title-line--lead title-line--lead-2">Found</span>
        <span class="title-line title-line--lead title-line--lead-3">The</span>
        <span class="title-line title-line--main title-line--main-1">Grey Orchard</span>
        <span class="title-line title-line--main title-line--main-2">Secret</span>
        <span class="title-line title-line--tail title-line--tail-1">We're</span>
        <span class="title-line title-line--tail title-line--tail-2">Dancing at Dusk</span>
      </h1>
    </section>
  </main>
</body>
</html>
```